tallow brook construction website (squarespace build)

construction website - see attached documents

Target Market(s)

owners, cm's, and gc's

Coding

Coded - Design and coding required

Font styles to use
Serif

Colors
0054AA
0677BA
7BADD7
CADEEF
E8F1F8

```html
<!DOCTYPE html>
<html lang="en">
<head>
<meta charset="utf-8">
<title>Tallow Brook Construction</title>
<link rel="stylesheet" href="https://fonts.googleapis.com/css2?family=Lora:wght@400;500;600;700&display=swap">
<style>
:root{
  --blue:#0054AA;
  --blue-2:#0677BA;
  --blue-3:#7BADD7;
  --blue-4:#CADEEF;
  --blue-5:#E8F1F8;
  --ink:#0b3566;
  --text:#33465e;
  --white:#ffffff;
}
*{box-sizing:border-box;margin:0;padding:0}
html,body{width:1200px;height:4552px;overflow:hidden}
body{font-family:'Lora',serif;color:var(--text);background:var(--white);position:relative}
.abs{position:absolute}
.photo{position:absolute;display:block}

/* header */
.site-header{position:absolute;left:0;top:0;width:1200px;height:85px;background:var(--white)}
.brand{position:absolute;left:92px;top:25px;display:flex;align-items:center;gap:12px;font-weight:700;font-size:26px;color:var(--blue);letter-spacing:.5px}
.brand-mark{width:20px;height:20px;background:var(--blue)}
.main-nav{position:absolute;left:418px;top:32px;font-size:13.5px;font-weight:500;color:var(--ink)}
.main-nav a{color:inherit;text-decoration:none;position:absolute;white-space:nowrap}
.nav-active{background:var(--blue);color:#fff!important;padding:3px 6px}
.quote-btn{position:absolute;left:986px;top:23px;width:122px;height:39px;background:var(--blue);color:#fff;font-size:13px;font-weight:600;display:flex;align-items:center;justify-content:center}

/* hero */
.hero{position:absolute;left:0;top:85px;width:1200px;height:634px;background:var(--blue)}
.hero-photo{left:590px;top:0;width:610px;height:634px;background:linear-gradient(160deg,#6f8fb0 0%,#9fb4c8 30%,#4e6783 60%,#2a3e58 100%)}
.hero-band{left:576px;top:0;width:14px;height:634px;background:var(--blue-2)}
.hero-eyebrow{left:110px;top:84px;color:#fff;font-size:14px;font-weight:700;letter-spacing:1px}
.hero-title{left:108px;top:114px;font-size:58px;line-height:60px;font-weight:700;color:#fff;letter-spacing:.5px}
.hero-title .muted{color:var(--blue-4)}
.hero-copy{left:110px;top:374px;width:390px;color:#fff;font-size:14.5px;line-height:26px;font-weight:500}
.btn-pair{display:flex;height:51px;border:2px solid #fff;font-size:14px;font-weight:700}
.btn-pair span{display:flex;align-items:center;padding:0 18px}
.btn-pair .on{background:#fff;color:var(--blue)}
.btn-pair .off{background:var(--blue);color:#fff}
.hero .btn-pair{position:absolute;left:110px;top:495px}

/* dividers */
.divider{position:absolute;display:flex;align-items:center;gap:8px}
.divider i{display:block;height:1.5px;background:var(--blue-3)}
.divider b{display:block;width:8px;height:8px;background:var(--blue-3);transform:rotate(45deg)}
.divider.light i,.divider.light b{background:#fff}

.sec-title{position:absolute;width:1200px;left:0;text-align:center;font-size:40px;font-weight:700;color:var(--blue)}
.sec-title .muted{color:var(--blue-3)}

/* about */
.about-title{left:599px;top:830px;font-size:38px;line-height:42px;font-weight:700;color:var(--blue)}
.about-title .muted{color:var(--blue-3)}
.about-copy{left:599px;top:964px;width:490px;font-size:15px;line-height:25.8px;text-align:justify;color:var(--text)}
.about-copy p+p{margin-top:25px}
.about .btn-pair{position:absolute;left:599px;top:1318px;border-color:var(--blue)}
.about .btn-pair .on{background:var(--blue);color:#fff}
.about .btn-pair .off{background:#fff;color:var(--blue)}

/* services */
.services{position:absolute;left:0;top:1493px;width:1200px;height:760px;background:var(--blue-5)}
.services-intro{position:absolute;left:270px;top:182px;width:660px;text-align:center;font-size:14.5px;line-height:27px;color:var(--text)}
.svc-card{position:absolute;top:267px;width:290px;height:396px;background:#fff;box-shadow:0 4px 14px rgba(0,84,170,.12);overflow:hidden}
.svc-photo{left:0;top:0;width:290px;height:178px}
.svc-icon{position:absolute;left:26px;top:143px;width:70px;height:70px;border-radius:50%;background:var(--blue);border:4px solid #fff;display:flex;align-items:center;justify-content:center}
.svc-card h3{position:absolute;left:25px;top:222px;width:250px;font-size:18px;line-height:27px;font-weight:600;color:var(--blue)}
.svc-card p{position:absolute;left:25px;top:280px;width:250px;font-size:13px;line-height:26px;color:var(--text)}
.svc-corner{position:absolute;right:0;bottom:0}
.slide-arrow{position:absolute;top:1934px;width:44px;height:44px;border:2px solid var(--blue-2);border-radius:50%;display:flex;align-items:center;justify-content:center}

/* markets */
.markets{position:absolute;left:0;top:2253px;width:1200px;height:684px;background:var(--blue)}
.markets .sec-title{color:#fff;top:73px}
.markets-copy{position:absolute;left:190px;top:175px;width:820px;text-align:center;color:#fff;font-size:14.5px;font-weight:500;line-height:26.5px}
.markets-sub{position:absolute;left:0;width:1200px;top:270px;text-align:center;color:#fff;font-size:22px;font-weight:500}
.mkt-box{position:absolute;top:355px;width:221px;height:202px;border:2px solid #fff;color:#fff;text-align:center}
.mkt-icon{position:absolute;left:80px;top:-24px;width:60px;height:44px;background:var(--blue);display:flex;justify-content:center;align-items:center}
.mkt-box h4{margin-top:42px;font-size:20px;font-weight:600}
.mkt-box p{margin:10px auto 0;width:190px;font-size:14px;line-height:26px;color:var(--blue-5)}
.dots{position:absolute;top:602px;left:584px;display:flex;gap:6px}
.dots span{width:11px;height:11px;border-radius:50%;background:var(--blue-3)}
.dots span:first-child{background:#fff}

/* projects */
.proj-photo{width:436px;height:413px}
.proj-caption{position:absolute;left:131px;top:3414px;width:434px;height:134px;background:var(--blue);clip-path:polygon(0 0,100% 0,100% 35%,80% 100%,0 100%);color:#fff;padding:22px 0 0 21px}
.proj-caption h5{font-size:16px;font-weight:700}
.proj-caption h5 small{font-size:12px}
.proj-caption p{font-size:12px;line-height:21px;margin-top:4px;width:270px;color:var(--blue-5)}

/* footer */
.site-footer{position:absolute;left:0;top:4130px;width:1200px;height:422px;background:var(--blue-5)}
.foot-brand{position:absolute;left:113px;top:112px;display:flex;align-items:center;gap:12px;font-size:34px;font-weight:700;color:var(--blue);line-height:40px}
.foot-brand .brand-mark{width:24px;height:24px}
.foot-col{position:absolute;top:82px}
.foot-col h6{font-size:18px;font-weight:700;color:var(--blue);margin-bottom:13px}
.foot-col li{list-style:none;font-size:15px;color:var(--ink);height:34.5px;display:flex;align-items:center;gap:10px}
.foot-col li::before{content:"";width:7px;height:7px;border-top:1.5px solid var(--blue-2);border-right:1.5px solid var(--blue-2);transform:rotate(45deg)}
.contact-row{display:flex;gap:14px;align-items:flex-start;font-size:15px;color:var(--ink);line-height:27px;margin-bottom:12px}
.ci{width:32px;height:32px;border-radius:50%;background:var(--blue);flex:none;display:flex;align-items:center;justify-content:center;margin-top:2px}
.foot-rule{position:absolute;left:110px;top:328px;width:979px;height:1px;background:var(--blue-3)}
.copyright{position:absolute;left:0;width:1200px;top:362px;text-align:center;font-size:15px;color:var(--ink);font-weight:500}
</style>
</head>
<body>

<header class="site-header">
  <div class="brand"><span class="brand-mark"></span>TALLOW BROOK</div>
  <nav class="main-nav">
    <a class="nav-active" style="left:0;top:-4px">HOME</a>
    <a style="left:79px">OUR SERVICES</a>
    <a style="left:211px">PROJECT PORFILIO</a>
    <a style="left:372px">MARKET</a>
    <a style="left:460px">CONTACT</a>
  </nav>
  <div class="quote-btn">GET A QUOTE</div>
</header>

<section class="hero">
  <div class="photo hero-photo" role="img" aria-label="Foundation crew working beside steel sheet piling on a wet excavation site"></div>
  <div class="abs hero-band"></div>
  <p class="abs hero-eyebrow">QUALITY STARTS AT THE FOUNDATION</p>
  <h1 class="abs hero-title">BUILDING<br><span class="muted">EXCELLENCE</span><br>THROUGH<br><span class="muted">EXPERIENCE.</span></h1>
  <p class="abs hero-copy">Tallow Brook Construction is a self-performing foundation and geotechnical general contractor and the critical first phase of every successful project.</p>
  <div class="btn-pair"><span class="on">VIEW OUR</span><span class="off">PROJECTS</span></div>
</section>

<section class="about">
  <div class="photo" style="left:111px;top:841px;width:325px;height:447px;background:linear-gradient(170deg,#d3dde9 0%,#93a9c2 45%,#50657e 100%)" role="img" aria-label="Workers in safety gear tying rebar on a tall reinforcement cage"></div>
  <div class="photo" style="left:277px;top:1067px;width:258px;height:302px;border:3px solid #fff;background:linear-gradient(180deg,#5a9ad6 0%,#c8a879 45%,#6b5a45 75%,#2b4b8a 100%)" role="img" aria-label="Multi-storey concrete building frame under construction behind a hoarding"></div>
  <h2 class="abs about-title">ABOUT TALLOW BROOK<br><span class="muted">CONSTRUCTION</span></h2>
  <div class="divider" style="left:599px;top:933px"><b></b><i style="width:140px"></i></div>
  <div class="abs about-copy">
    <p>Tallow Brook partners with owners, construction managers, and general contractors from design through construction delivery. Our team supports projects at every phase — preconstruction, engineering and design support, exploratory investigations, design proof testing, and complete structural packages for our clients. Tallow Brook brings precision, accountability, and true partnership to ground-level work — because what's below the surface determines everything above it.</p>
    <p>Our projects managed and built by experienced professionals and skilled craftsmen, we hold safety and quality to the highest standard expected in the New York City and across the tri-state market.</p>
  </div>
  <div class="btn-pair"><span class="on">LEARN MORE</span><span class="off">ABOUT US</span></div>
</section>

<section class="services">
  <h2 class="sec-title" style="top:80px">OUR <span class="muted">SERVICES</span></h2>
  <div class="divider" style="left:522px;top:145px"><i style="width:70px"></i><b></b><i style="width:70px"></i></div>
  <p class="services-intro">Tallow Brook brings precision, accountability, and true partnership to ground-level work — because what's below the surface determines everything above it.</p>

  <article class="svc-card" style="left:110px">
    <div class="photo svc-photo" style="background:linear-gradient(180deg,#a57a4d,#7a5432 60%,#9c6b44)" role="img" aria-label="Timber formwork walls around an excavated foundation"></div>
    <div class="svc-icon"><svg width="34" height="34" viewBox="0 0 34 34" aria-hidden="true" fill="none" stroke="#fff" stroke-width="2"><rect x="11" y="3" width="12" height="12" rx="2"/><circle cx="7" cy="26" r="4"/><circle cx="17" cy="26" r="4"/><circle cx="27" cy="26" r="4"/><path d="M17 15v7"/></svg></div>
    <h3>Owner, CM's, and GC's Services</h3>
    <p>Complete turnkey site &amp; structural packages. Site constructability and logistical assessments. Value engineering.</p>
    <svg class="svc-corner" width="64" height="34" viewBox="0 0 64 34" aria-hidden="true"><polygon points="64,0 64,34 0,34" fill="#0054AA"/><path d="M36 24h16M46 18l6 6-6 6" stroke="#fff" stroke-width="2.4" fill="none"/></svg>
  </article>

  <article class="svc-card" style="left:454px">
    <div class="photo svc-photo" style="background:linear-gradient(180deg,#8c8f94,#b3aea4 50%,#6f6a60)" role="img" aria-label="Excavation pit with concrete retaining walls and steel supports"></div>
    <div class="svc-icon"><svg width="34" height="34" viewBox="0 0 34 34" aria-hidden="true" fill="#fff"><path d="M3 26h16v5H3z"/><path d="M6 26l3-8h7l2 8z"/><path d="M16 18l8-10 6 4-3 2-4-2-5 8z"/></svg></div>
    <h3>Foundation &amp; Earth Retention</h3>
    <p>Foundation &amp; Excavation. Driven &amp; Drilled Pile Systems. Helical Piles Auger Cast Piles. Hollow Bar &amp; Needle Systems.</p>
    <svg class="svc-corner" width="64" height="34" viewBox="0 0 64 34" aria-hidden="true"><polygon points="64,0 64,34 0,34" fill="#0054AA"/><path d="M36 24h16M46 18l6 6-6 6" stroke="#fff" stroke-width="2.4" fill="none"/></svg>
  </article>

  <article class="svc-card" style="left:797px">
    <div class="photo svc-photo" style="background:linear-gradient(180deg,#6e7783,#9aa1a8 55%,#585f66)" role="img" aria-label="Poured concrete slab and walls in a site basement"></div>
    <div class="svc-icon"><svg width="34" height="34" viewBox="0 0 34 34" aria-hidden="true" fill="none" stroke="#fff" stroke-width="2"><path d="M6 6h22M10 6v24M10 10l8-4"/><rect x="16" y="16" width="12" height="14"/><path d="M19 20h2M23 20h2M19 25h2M23 25h2"/></svg></div>
    <h3>Reinforced Concrete &amp; Site Services</h3>
    <p>Reinforced Concrete Structures Masonry. Shotcrete. Sitework De-Watering. DemolitionSlab on Grade</p>
    <svg class="svc-corner" width="64" height="34" viewBox="0 0 64 34" aria-hidden="true"><polygon points="64,0 64,34 0,34" fill="#0054AA"/><path d="M36 24h16M46 18l6 6-6 6" stroke="#fff" stroke-width="2.4" fill="none"/></svg>
  </article>
</section>

<div class="slide-arrow" style="left:31px"><svg width="20" height="16" viewBox="0 0 20 16" aria-hidden="true"><path d="M18 8H3M9 2L3 8l6 6" stroke="#0677BA" stroke-width="2" fill="none"/></svg></div>
<div class="slide-arrow" style="left:1119px"><svg width="20" height="16" viewBox="0 0 20 16" aria-hidden="true"><path d="M2 8h15M11 2l6 6-6 6" stroke="#0677BA" stroke-width="2" fill="none"/></svg></div>

<section class="markets">
  <h2 class="sec-title">MARKETS &amp; INDUSTRIES</h2>
  <div class="divider light" style="left:522px;top:130px"><i style="width:70px"></i><b></b><i style="width:70px"></i></div>
  <p class="markets-copy">Tallow Brook Construction serves owners, construction managers, and general contractors and subcontractors across the New York, New Jersey, and Connecticut tri-state region. Our self-performing model allows us to support projects of every scale and complexity throughout the region.</p>
  <p class="markets-sub">Markets We Serve</p>

  <div class="mkt-box" style="left:111px">
    <div class="mkt-icon"><svg width="34" height="34" viewBox="0 0 34 34" aria-hidden="true" fill="#fff"><rect x="9" y="4" width="16" height="28"/><g fill="#0054AA"><rect x="12" y="8" width="3" height="3"/><rect x="19" y="8" width="3" height="3"/><rect x="12" y="14" width="3" height="3"/><rect x="19" y="14" width="3" height="3"/><rect x="12" y="20" width="3" height="3"/><rect x="19" y="20" width="3" height="3"/><rect x="15" y="26" width="4" height="6"/></g><rect x="4" y="31" width="26" height="2"/></svg></div>
    <h4>Commercial</h4>
    <p>Office, retail, and mixed-use foundation and structural packages</p>
  </div>
  <div class="mkt-box" style="left:362px">
    <div class="mkt-icon"><svg width="34" height="34" viewBox="0 0 34 34" aria-hidden="true" fill="#fff"><path d="M3 16L17 4l14 12h-4v15H7V16z"/><rect x="14" y="22" width="6" height="9" fill="#0054AA"/></svg></div>
    <h4>Residential</h4>
    <p>Multi-family and single-family foundation, underpinning, and earth-retention work</p>
  </div>
  <div class="mkt-box" style="left:615px">
    <div class="mkt-icon"><svg width="34" height="34" viewBox="0 0 34 34" aria-hidden="true" fill="#fff"><path d="M3 32V16l8 5v-5l8 5v-5l8 5V4h4v28z"/><g fill="#0054AA"><rect x="7" y="24" width="3" height="3"/><rect x="14" y="24" width="3" height="3"/><rect x="21" y="24" width="3" height="3"/></g></svg></div>
    <h4>Industrial</h4>
    <p>Warehouse and distribution center foundation systems, including complete</p>
  </div>
  <div class="mkt-box" style="left:866px">
    <div class="mkt-icon"><svg width="34" height="34" viewBox="0 0 34 34" aria-hidden="true" fill="#fff"><path d="M12 8h10v6h8v18H4V14h8z"/><rect x="15" y="2" width="4" height="6"/><g fill="#0054AA"><rect x="7" y="18" width="3" height="3"/><rect x="24" y="18" width="3" height="3"/><rect x="7" y="24" width="3" height="3"/><rect x="24" y="24" width="3" height="3"/><rect x="15" y="12" width="4" height="4"/><rect x="15" y="24" width="4" height="8"/></g></svg></div>
    <h4>Institutional</h4>
    <p>Healthcare, education, and government facility foundation work</p>
  </div>
  <div class="dots"><span></span><span></span></div>
</section>

<section class="projects">
  <h2 class="sec-title" style="top:3012px">OUR <span class="muted">PROJECTS</span></h2>
  <div class="divider" style="left:522px;top:3078px"><i style="width:70px"></i><b></b><i style="width:70px"></i></div>
  <div class="photo proj-photo" style="left:131px;top:3140px;background:linear-gradient(160deg,#b5713a,#d59a5e 40%,#7a4526)" role="img" aria-label="Framers in hard hats working inside a timber house frame"></div>
  <div class="proj-caption">
    <h5>RESIDENTIAL FOUNDATION <small>($3.8 MILLION)</small></h5>
    <p>End-to-end foundation construction for a multi-family housing project.<br>Client Name: Harlow Development Group<br>Delivered on schedule.</p>
  </div>
  <div class="photo proj-photo" style="left:634px;top:3140px;background:linear-gradient(160deg,#3f8fb3,#86c0d6 45%,#c9a64b 75%,#46535f)" role="img" aria-label="Engineers in hard hats reviewing a site beside a tower crane"></div>
  <div class="photo proj-photo" style="left:131px;top:3610px;background:linear-gradient(180deg,#8fa6bc,#a08a6a 50%,#6c6456)" role="img" aria-label="Three site supervisors in high-visibility vests walking on a scaffolded site"></div>
  <div class="photo proj-photo" style="left:634px;top:3610px;background:linear-gradient(170deg,#3f6ea8,#7b98b6 45%,#b47b48 75%,#3a2f28)" role="img" aria-label="Concrete building frame and crane at sunset"></div>
</section>

<footer class="site-footer">
  <div class="foot-brand"><span class="brand-mark"></span>TALLOW<br>BROOK</div>
  <div class="foot-col" style="left:419px">
    <h6>QUICK LINKS</h6>
    <ul><li>Home</li><li>Our Services</li><li>Project Portfolio</li><li>Market</li><li>Contact Us</li></ul>
  </div>
  <div class="foot-col" style="left:643px">
    <h6>HELP LINKS</h6>
    <ul><li>FAQ</li><li>Terms of use</li><li>Privacy Policy</li><li>Support Links</li><li>Conditions</li></ul>
  </div>
  <div class="foot-col" style="left:864px">
    <h6>CONTACT US</h6>
    <div class="contact-row"><span class="ci"><svg width="14" height="18" viewBox="0 0 14 18" aria-hidden="true"><path d="M7 1a6 6 0 016 6c0 4-6 10-6 10S1 11 1 7a6 6 0 016-6z" fill="#fff"/><circle cx="7" cy="7" r="2.2" fill="#0054AA"/></svg></span><span>Tallow Brook<br>United States</span></div>
    <div class="contact-row"><span class="ci"><svg width="16" height="16" viewBox="0 0 16 16" aria-hidden="true"><path d="M4 1l3 3-2 2c1 2 3 4 5 5l2-2 3 3-2 3C7 15 1 9 1 3z" fill="#fff"/></svg></span><span style="margin-top:3px">+1 555 014 2290</span></div>
    <div class="contact-row"><span class="ci"><svg width="16" height="12" viewBox="0 0 16 12" aria-hidden="true"><rect x="0" y="0" width="16" height="12" rx="1" fill="#fff"/><path d="M1 1l7 6 7-6" stroke="#0054AA" stroke-width="1.5" fill="none"/></svg></span><span style="margin-top:3px">info@tallowbrook.com</span></div>
  </div>
  <div class="foot-rule"></div>
  <p class="copyright">Copyrights@2026.Tallow Brook.All Rights Reserved</p>
</footer>

</body>
</html>
```